Vital Spark Electrical in need of a business card design

We need a new business card designed for our electrical business. We have a logo already which I will attach below.
Would like the business card to be..
-BLACK background preferably, possibly white back ground behind logo if colours clash.
-White & Blue (logo blue) text
Something that makes the logo pop, & a modern look. Possibly minimal clean format.

REQUIRE:
-Logo on front & back

TEXT TO INCLUDE (ON ONE SIDE):

Tom Harlow
Director/Electrician
M: 0417 365 208
E:info@vitalsparkelectrical-example.com.au
W:www.vitalsparkelectrical-example.com.au
R.E.C 57318

Custom/New Homes
Renovations
Commercial Office/Shop Fit-outs
Communications & Security Cameras
Electric Vehicle Chargers
Airconditioning
Updates

Requirements
Nice to have
• Possibly even lighten the grey shades for the words 'Vital' & 'Spark' to be more easily read on a black background.

```html
<!DOCTYPE html>
<html lang="en">
<head>
<meta charset="utf-8">
<title>Vital Spark Electrical – Business Card</title>
<link rel="stylesheet" href="https://fonts.googleapis.com/css2?family=Open+Sans:wght@400;600;700&display=swap">
<style>
  :root {
    --page-bg: #3a3a38;
    --card-black: #111213;
    --card-edge: #1c1d1f;
    --logo-blue: #3aa6dc;
    --text-grey: #a9acb0;
    --text-light: #d4d6d8;
  }
  * { box-sizing: border-box; margin: 0; padding: 0; }
  html, body {
    width: 1200px; height: 824px; overflow: hidden;
    background: var(--page-bg);
    font-family: "Open Sans", Arial, sans-serif;
  }
  .canvas {
    position: relative; width: 1200px; height: 824px;
    display: flex; align-items: center; justify-content: center; gap: 40px;
  }
  .card {
    position: relative; width: 540px; height: 310px;
    background: var(--card-black);
    border: 1px solid var(--card-edge);
    border-radius: 3px;
    overflow: hidden;
  }

  /* Back side: services + brand */
  .services {
    position: absolute; left: 28px; top: 26px;
    list-style: none;
  }
  .services li {
    display: flex; align-items: center; gap: 7px;
    font-size: 11.5px; color: var(--text-grey);
    line-height: 20px;
  }
  .services .tick { width: 11px; height: 11px; flex: none; }
  .brand-large {
    position: absolute; left: 200px; top: 170px;
    display: flex; align-items: center; gap: 16px;
  }
  .brand-large .brand-square {
    width: 46px; height: 46px; background: var(--logo-blue);
  }
  .brand-large .brand-name {
    font-size: 30px; font-weight: 600; color: var(--text-light);
    line-height: 1.05;
  }

  /* Front side: brand + contact */
  .brand-small {
    position: absolute; left: 28px; top: 122px;
    display: flex; align-items: center; gap: 10px;
  }
  .brand-small .brand-square {
    width: 22px; height: 22px; background: var(--logo-blue);
  }
  .brand-small .brand-name {
    font-size: 17px; font-weight: 600; color: var(--text-light);
    line-height: 1.1;
  }
  .contact {
    position: absolute; left: 236px; right: 20px; top: 92px;
  }
  .contact .person-name {
    font-size: 21px; font-weight: 700; color: var(--text-grey);
    letter-spacing: 0.5px;
  }
  .contact .role, .contact .licence {
    font-size: 13px; color: var(--logo-blue); line-height: 17px;
  }
  .contact .details { list-style: none; margin-top: 12px; }
  .contact .details li {
    display: flex; align-items: center; gap: 8px;
    font-size: 11.5px; color: var(--text-grey); line-height: 21px;
    white-space: nowrap;
  }
  .contact .icon { width: 12px; height: 12px; flex: none; fill: var(--logo-blue); }
</style>
</head>
<body>
<main class="canvas">

  <section class="card card-back" aria-label="Card back">
    <ul class="services">
      <li><svg class="tick" viewBox="0 0 12 12"><path d="M1.5 6.5l3 3 6-7" fill="none" stroke="#3aa6dc" stroke-width="2"/></svg>Custom/New Homes</li>
      <li><svg class="tick" viewBox="0 0 12 12"><path d="M1.5 6.5l3 3 6-7" fill="none" stroke="#3aa6dc" stroke-width="2"/></svg>Renovations</li>
      <li><svg class="tick" viewBox="0 0 12 12"><path d="M1.5 6.5l3 3 6-7" fill="none" stroke="#3aa6dc" stroke-width="2"/></svg>Commercial Office/Shop Fit-outs</li>
      <li><svg class="tick" viewBox="0 0 12 12"><path d="M1.5 6.5l3 3 6-7" fill="none" stroke="#3aa6dc" stroke-width="2"/></svg>Communications &amp; Security Cameras</li>
      <li><svg class="tick" viewBox="0 0 12 12"><path d="M1.5 6.5l3 3 6-7" fill="none" stroke="#3aa6dc" stroke-width="2"/></svg>Electric Vehicle Chargers</li>
      <li><svg class="tick" viewBox="0 0 12 12"><path d="M1.5 6.5l3 3 6-7" fill="none" stroke="#3aa6dc" stroke-width="2"/></svg>Airconditioning</li>
    </ul>
    <div class="brand-large">
      <span class="brand-square"></span>
      <span class="brand-name">Vital Spark<br>Electrical</span>
    </div>
  </section>

  <section class="card card-front" aria-label="Card front">
    <div class="brand-small">
      <span class="brand-square"></span>
      <span class="brand-name">Vital Spark<br>Electrical</span>
    </div>
    <div class="contact">
      <p class="person-name">Tom Harlow</p>
      <p class="role">Director/Electrician</p>
      <p class="licence">R.E.C 57318</p>
      <ul class="details">
        <li><svg class="icon" viewBox="0 0 12 12"><path d="M2.5 1h2l1 3-1.4 1a6.5 6.5 0 0 0 2.9 2.9l1-1.4 3 1v2c0 .8-.7 1.5-1.5 1.5A9.5 9.5 0 0 1 1 2.5C1 1.7 1.7 1 2.5 1z"/></svg>0417 365 208</li>
        <li><svg class="icon" viewBox="0 0 12 12"><path d="M0.5 2.5h11v7h-11z"/><path d="M0.8 2.8l5.2 4 5.2-4" fill="none" stroke="#111213" stroke-width="1"/></svg>info@vitalsparkelectrical-example.com.au</li>
        <li><svg class="icon" viewBox="0 0 12 12"><circle cx="6" cy="6" r="5.2"/><path d="M6 0.8v10.4M0.8 6h10.4M6 0.8c-3 3-3 7.4 0 10.4M6 0.8c3 3 3 7.4 0 10.4" fill="none" stroke="#111213" stroke-width="0.8"/></svg>www.vitalsparkelectrical-example.com.au</li>
      </ul>
    </div>
  </section>

</main>
</body>
</html>
```